Clean Plinth Ads Banner Design For A Finance Company

Hi,
We're a UK based finance company and are looking for new banner ads to use on the Plinth Display Network.
We want the end product to stand out by using strong, minimal design - ideally starting from a dark theme, although I'm open to ideas.
The copy should read:
'Fast Bridging Loans From 0.39% PM'
Once we have these designs agreed, we are looking to replicate them for other products, changing only the text on each ad - for example, 'commercial mortgage service you can rely on' or 'development finance service you can rely on'.
The colours used on our website are the following:
Black - #040303
Orange - #f79124
White - #ffffff
Grey - #ffffff
Example ads that I like - https://www.brimcastle.com/wp-content/uploads/2021/07/plinth-display-ads-example-2-final.png.webp
2 - https://quendrahub.com/wp-content/uploads/2020/03/fbdd56ba3bd16c7a8debb13a411de786.jpg

```html
<!DOCTYPE html>
<html lang="en">
<head>
<meta charset="utf-8">
<title>Corvane Finance – Bridging Loan Banners</title>
<link rel="stylesheet" href="https://fonts.googleapis.com/css2?family=Open+Sans:wght@400;600;700&display=swap">
<style>
  :root {
    --canvas-bg: #d6994f;
    --brand-black: #040303;
    --brand-orange: #f79124;
    --brand-white: #ffffff;
    --glow-orange: #b8641a;
    --glow-deep: #4a2a0c;
    --photo-light: #8a6a4a;
    --photo-mid: #5e4430;
    --photo-deep: #2a1d12;
  }
  * { box-sizing: border-box; margin: 0; padding: 0; }
  html, body {
    width: 1200px;
    height: 1200px;
    overflow: hidden;
  }
  body {
    background: var(--canvas-bg);
    font-family: "Open Sans", Arial, sans-serif;
    color: var(--brand-white);
    position: relative;
  }
  .banner {
    position: absolute;
    background: var(--brand-black);
    overflow: hidden;
    text-align: center;
  }
  .banner > * { position: absolute; left: 0; right: 0; }

  .headline { font-weight: 400; letter-spacing: 0.5px; }
  .headline strong { font-weight: 700; }
  .rate { font-weight: 700; }
  .rate .rate-value { color: var(--brand-orange); }
  .cta {
    display: flex;
    align-items: center;
    justify-content: center;
    background: var(--brand-orange);
    color: var(--brand-white);
    font-weight: 700;
    letter-spacing: 1px;
    text-transform: uppercase;
    text-decoration: none;
  }
  .brand {
    color: var(--brand-orange);
    font-weight: 700;
    line-height: 1;
  }
  .brand .brand-name { display: block; letter-spacing: 1px; }
  .brand .brand-suffix { display: block; }

  /* Skyscraper banner */
  .banner--skyscraper { left: 213px; top: 131px; width: 249px; height: 937px; }
  .banner--skyscraper .headline {
    top: 63px;
    font-size: 42px;
    line-height: 50px;
  }
  .banner--skyscraper .rate {
    top: 276px;
    font-size: 46px;
    line-height: 53px;
  }
  .banner--skyscraper .cta {
    left: 58px; right: auto;
    top: 430px;
    width: 138px; height: 39px;
    font-size: 13px;
  }
  .banner--skyscraper .visual {
    top: 560px;
    height: 360px;
    background: radial-gradient(ellipse 70% 45% at 50% 38%, var(--glow-orange) 0%, var(--glow-deep) 45%, var(--brand-black) 85%);
  }
  .banner--skyscraper .brand { top: 828px; }
  .banner--skyscraper .brand-name { font-size: 38px; }
  .banner--skyscraper .brand-suffix { font-size: 14px; margin-top: 8px; }

  /* Half-page banner */
  .banner--halfpage { left: 520px; top: 134px; width: 466px; height: 930px; }
  .banner--halfpage .headline {
    top: 102px;
    font-size: 58px;
    line-height: 63px;
  }
  .banner--halfpage .rate {
    top: 252px;
    font-size: 67px;
    line-height: 76px;
  }
  .banner--halfpage .cta {
    left: 113px; right: auto;
    top: 376px;
    width: 246px; height: 69px;
    font-size: 24px;
  }
  .banner--halfpage .visual {
    top: 470px;
    bottom: 0;
    background:
      linear-gradient(180deg, var(--brand-black) 0%, rgba(4,3,3,0) 35%),
      radial-gradient(ellipse 55% 45% at 35% 45%, var(--photo-light) 0%, rgba(138,106,74,0) 100%),
      linear-gradient(100deg, var(--photo-mid) 0%, #6e5036 45%, #4a3320 75%, var(--photo-deep) 100%);
  }
  .banner--halfpage .brand { top: 792px; }
  .banner--halfpage .brand-name { font-size: 56px; }
  .banner--halfpage .brand-suffix { font-size: 20px; margin-top: 10px; }
</style>
</head>
<body>

  <section class="banner banner--skyscraper" aria-label="Bridging loans skyscraper banner">
    <h1 class="headline"><strong>Fast</strong><br>Bridging<br>Loans<br>From</h1>
    <p class="rate"><span class="rate-value">0.39%</span><br>PM</p>
    <a class="cta">Learn More</a>
    <div class="visual" role="img" aria-label="Hand holding a small model house with a warm orange glow behind it"></div>
    <p class="brand"><span class="brand-name">Corvane</span><span class="brand-suffix">Finance Limited</span></p>
  </section>

  <section class="banner banner--halfpage" aria-label="Bridging loans half-page banner">
    <h1 class="headline"><strong>Fast</strong> Bridging<br>Loans From</h1>
    <p class="rate"><span class="rate-value">0.39%</span> PM</p>
    <a class="cta">Learn More</a>
    <div class="visual" role="img" aria-label="Warm-toned photo of a smiling couple meeting with a finance adviser"></div>
    <p class="brand"><span class="brand-name">Corvane</span><span class="brand-suffix">Finance Limited</span></p>
  </section>

</body>
</html>
```